"Zarvo! Brush" retail packaging for a non chemical teeth whitening brush

I need new retail Blister packaging design for the "Zarvo! Brush"
The product name "Zarvo! Brush" is Trademarked.
The reason we called it Zarvo Brush is that is a play on the words of Tooth Brush and the Zarvo! refers to a word used with magic like "zarvo! the rabbit is gone!" In our case Zarvo! the stains on your teeth are gone!
So we are looking for a magic themed design.

Package dimensions 81 by 138 cm (packaging being used is in the picture labeled "zarvo flyer".

The front of the packaging needs to contain the following information:

Zarvo! Brush
Naturally Whitens Teeth*
Quickly removes stains from coffee, cola, tea, tobacco, and wine.
Includes 1 brush with 6 refills

(put the " *whitens by removing stains on teeth" in small print somewhere out of the way)
Would like to include the following on front of package but if too crowded ok to omit:

Microbristle Technology
No Chemicals
Zarvobrush.com

Attached our some examples and files of previously badly designed packaged product.

The current product is the one with a brush and 6 refills.

The back of the product needs the pictures included on the back of the packaging in the picture "zarvo flyer". The back of package will be in black and white and needs areas for instructions of how to refill brush, Instructions of use, other info including company info and UPC code. This information will be included later.
You will need to get the pictures for the back of the packaging off the included picture "zarvo flyer" I do not have original files.
place on top of the back of product
" * whitens by removing stains on teeth"

Measurement UPDATE:

New product Dimensions 81 by 138mm make sure to give a few extra mm's of background to accommodate die cutting of product!

Measurements of where blister is located on product:

There are 2 sets of measurements. 1 set for where blister begins and 1 set of where background graphics can still be seen behind blister.

1st set of measurements are where blister begins and gives you area where wording can be placed:

66mm from top of card
13mm from bottom of card
7mm from side of card

2nd set of measurements are where graphics can still be seen but wording should not be placed in between 1st set of measurements and 2nd set listed below:

71mm from top of card
18mm from bottom of card
15mm from sides of card

Make sure to place blister of product correctly in you design. Every mm of accuracy is important.
Updates

The dimensions of the product are 138x83 mm's but the graphic should extend a few mm's past this to account for die cutting.  All important graphics and text should be contained in the 138x83 mm dimensions.

The back of the product is in Black and White.  The pictures on the back of the product in the file "zarvo flyer" need to be taken off that picture and put on the new packaging graphics.   I will provide specific text for the back of the product in the next few days along with company info and upc code.

The New packaging and dimensions are in File 3 "zarvo flyer"

The picture in File 1 is old packaging and old product and is included just for reference.                               

The picture in File 2 is the product in the package that we want the new design for.                                     

The brief was slightly edited so please read brief again.   Changes were made for wording on the front of the package.

Important dimensions update: Please re-read brief...

product size changed to 81x 138mm

I also included photos of package with measurements of where blister is on package.

I will provide details about back of product soon..

 We have been getting a lot of designs similar to the old ones. 

No designs similar to the old ones.....please no pictures of people in design....unless you have some type of amazing concept that will prove otherwise.

We added a photo titled "magic"  for inspiration.  We are looking for a elegant clean magic theme.

 Change we will now be putting the "*whitens by removing stains on teeth"  to the top of the back of the package.

We added a 2nd place payout!

Target Market(s)

Target market are teenagers and adults who are concerned about appearance and drink, eat and smoke things that stain teeth.

Industry/Entity Type

It Company

Requirements
Must have
• Magic Theme to tie in the word Zarvo! with the product.
Make it obvious what product does!
Should not have
• Naked women or men ;)
No pictures of people! Unless you have an amazing concept that will change things!

```html
<!DOCTYPE html>
<html lang="en">
<head>
<meta charset="utf-8">
<title>Zarvo! Brush – Blister Card Front</title>
<link href="https://fonts.googleapis.com/css2?family=Arimo:ital,wght@0,400;0,700;1,400&display=swap" rel="stylesheet">
<style>
  :root {
    --backdrop: #e9ecee;
    --card-top: #3bb8ec;
    --card-mid: #1a78c6;
    --card-low: #1660ad;
    --card-bottom: #0f4c96;
    --glow: rgba(255, 255, 255, 0.55);
    --ray: rgba(255, 255, 255, 0.10);
    --white: #ffffff;
    --claim-ink: #eef0ff;
    --claim-edge: #1d2c7e;
    --banner-red: #e8313a;
    --brand-red: #e8313a;
    --magic-violet: #9b3a9c;
    --hang-hole: #0d0d0d;
    --tooth-tone: #f2f6fb;
  }
  * { box-sizing: border-box; margin: 0; padding: 0; }
  html, body {
    width: 1200px; height: 900px; overflow: hidden;
    background: var(--backdrop);
    font-family: "Arimo", Arial, sans-serif;
  }
  .canvas { position: relative; width: 1200px; height: 900px; }

  .card {
    position: absolute; left: 340px; top: 42px;
    width: 477px; height: 813px; overflow: hidden;
    background:
      radial-gradient(ellipse 300px 260px at 55% 26%, var(--glow), rgba(255,255,255,0) 70%),
      radial-gradient(ellipse 420px 520px at 55% 30%, var(--ray), rgba(255,255,255,0) 75%),
      linear-gradient(180deg, var(--card-top) 0%, var(--card-mid) 45%, var(--card-low) 70%, var(--card-bottom) 100%);
    color: var(--white);
  }
  .card > * { position: absolute; }

  .hang-hole { left: 186px; top: 49px; width: 112px; height: 42px; }

  .magic-glow {
    left: 40px; top: 110px; width: 440px; height: 150px;
    background: radial-gradient(ellipse at 50% 55%, rgba(155,58,156,0.22), rgba(155,58,156,0) 65%);
  }

  .brand-name {
    left: 24px; width: 477px; top: 148px;
    text-align: center;
    font-size: 58px; font-weight: 700; letter-spacing: 1px;
    color: var(--brand-red);
  }

  .claim {
    left: 62px; width: 400px; top: 233px; text-align: center;
    font-size: 19px; font-weight: 400; color: var(--claim-ink);
    text-shadow: 0 0 2px var(--claim-edge), 0 0 1px var(--claim-edge);
  }
  .claim-note {
    left: 62px; width: 400px; top: 258px; text-align: center;
    font-size: 13.5px; color: var(--white);
  }
  .sparkle-line { top: 239px; width: 60px; height: 10px; }
  .sparkle-line.left { left: 90px; }
  .sparkle-line.right { left: 375px; }

  .mascot-area {
    left: 52px; top: 276px; width: 88px; height: 104px;
    border-radius: 38px 38px 30px 30px;
    background: linear-gradient(160deg, var(--tooth-tone), #c9dcf0);
  }

  .stain-banner { left: 128px; top: 314px; width: 316px; height: 46px; }
  .stain-text {
    left: 149px; top: 316px; width: 300px;
    font-size: 16.5px; line-height: 20px; color: var(--white);
  }

  .features {
    left: 70px; top: 387px; width: 380px;
    display: flex; gap: 30px;
    font-size: 16.3px; list-style: none;
  }
  .features li::before { content: "★"; font-size: 10px; margin-right: 5px; vertical-align: 2px; }

  .blister-window {
    left: 60px; top: 443px; width: 359px; height: 306px;
    border: 2px solid var(--white); border-radius: 11px;
  }

  .contents-note {
    left: 449px; top: 612px;
    transform: translate(-50%, -50%) rotate(-90deg);
    white-space: nowrap;
    font-size: 16px;
  }

  .website {
    left: 68px; top: 768px;
    font-size: 17px; font-style: italic; letter-spacing: 0.2px;
  }
</style>
</head>
<body>
<main class="canvas">
  <section class="card" aria-label="Zarvo! Brush blister card front">
    <svg class="hang-hole" viewBox="0 0 112 42" aria-hidden="true">
      <path fill="var(--hang-hole)" d="M10 14 H40 C44 14 46 2 56 2 C66 2 68 14 72 14 H102 C108 14 112 18 112 24 V32 C112 38 108 42 102 42 H10 C4 42 0 38 0 32 V24 C0 18 4 14 10 14 Z"/>
    </svg>

    <div class="magic-glow" role="img" aria-label="Magic burst of violet sparks around the product name"></div>

    <h1 class="brand-name">Zarvo! Brush</h1>

    <svg class="sparkle-line left" viewBox="0 0 60 10" aria-hidden="true">
      <polygon fill="var(--white)" points="0,5 60,1 54,5 60,9"/>
    </svg>
    <p class="claim">Naturally Whitens Teeth</p>
    <svg class="sparkle-line right" viewBox="0 0 60 10" aria-hidden="true">
      <polygon fill="var(--white)" points="60,5 0,1 6,5 0,9"/>
    </svg>
    <p class="claim-note">whitens by removing stains on teeth</p>

    <div class="mascot-area" role="img" aria-label="Smiling cartoon tooth mascot with a sparkle"></div>

    <svg class="stain-banner" viewBox="0 0 316 46" aria-hidden="true">
      <polygon fill="var(--banner-red)" points="14,2 316,0 302,46 0,46"/>
    </svg>
    <p class="stain-text">Quickly removes stains from<br>coffee, cola, tea, tobacco, and wine.</p>

    <ul class="features">
      <li>Microbristle Technology</li>
      <li>No Chemicals</li>
    </ul>

    <div class="blister-window" aria-label="Blister window"></div>

    <p class="contents-note">Includes 1 brush with 6 refills</p>

    <p class="website">zarvobrush.com</p>
  </section>
</main>
</body>
</html>
```